Fahrzeugbeschriftung für Software-Dienstleister in der Automation (Robotik)
Zielgruppe
Ich bin freier Softwareentwickler für Industrielle Automationslösungen. Im Klartext bedeutet das, ich schreibe Software für Roboter- und SPS-Steuerungen. Meine Zielgruppe ist sowohl der klassische Maschinenbau (10-500 Mitarbeiter) als auch die Industrie (Automobilbau, Lebensmittelindustrie, Konsumgüter, usw.)
Neben der Softwareentwicklung biete ich meinen Kunden auch Schulungen zum Thema Roboter-Programmierung, sowie Wartung von Industrierobotern an.
Aufgabenstellung
Ich möchte nicht das komplette Fahrzeug als Werbefläche nutzen, das hatte ich bereits in der Vergangenheit. Von meinen Bestandskunden wurde ich zwar auf das Fahrzeug angesprochen, es hat sich jedoch nie ein Neukunde aufgrund der Fahrzeugwerbung gemeldet. Mir geht es vielmehr um einen dezenten, aber dennoch aussagekräftigen Hinweis auf meine Tätigkeiten. Ich stehe mit meinem Fahrzeug regelmäßig bei einem Roboter-Hersteller auf dem Parkplatz, dort laufen täglich mehrere potentielle Kunden direkt an meinem Fahrzeug vorbei. Das heißt, es wird keine Werbung benötigt, die auch bei 50km/h noch zu erkennen ist. Ein Hinweis auf dem Heck würde reichen...
Beim Fahrzeug handelt es sich um den Brenz Valora S-Trim in weiß.
Im Anhang befindet sich das Logo, das aktuelle Design meiner Visitenkarten sowie Bilder (quarzo) vom Fahrzeug, weitere Informationen gibt es auf der Homepage unter www.tk-fertigwerk.net.

```html
<!DOCTYPE html>
<html lang="de">
<head>
<meta charset="utf-8">
<title>tk fertigwerk – Heckbeschriftung</title>
<link href="https://fonts.googleapis.com/css2?family=Ubuntu:wght@400;500;700&display=swap" rel="stylesheet">
<style>
  :root {
    --lime: #afca0b;
    --ink: #252525;
    --panel: #ffffff;
    --stage: #434343;
    --bar: #262626;
  }
  * { margin: 0; padding: 0; box-sizing: border-box; }
  html, body { width: 1200px; height: 675px; overflow: hidden; }
  body {
    background: var(--stage);
    font-family: "Ubuntu", sans-serif;
    position: relative;
  }
  .decal {
    position: absolute;
    left: 32px; top: 53px;
    width: 1136px; height: 568px;
    background: var(--panel);
    overflow: hidden;
  }
  .headline { position: absolute; left: 0; top: 0; width: 740px; height: 240px; }
  .headline text { font-family: "Ubuntu", sans-serif; font-weight: 700; fill: #fff; }
  .brand {
    position: absolute;
    right: 22px; top: 80px;
    text-align: right;
  }
  .brand-name {
    font-size: 50px; font-weight: 500; color: var(--ink);
    line-height: 1; letter-spacing: 0.5px;
  }
  .brand-claim {
    margin-top: 14px;
    font-size: 21px; font-weight: 400; color: var(--lime);
    letter-spacing: 2.6px; line-height: 1;
  }
  .services {
    position: absolute; left: 56px; top: 262px;
    list-style: none;
  }
  .services li {
    display: flex; align-items: center;
    height: 52px;
    font-size: 31px; color: var(--ink);
  }
  .services svg { width: 27px; height: 27px; margin-right: 20px; flex: none; }
  .contact-bar {
    position: absolute; left: 0; top: 459px;
    width: 100%; height: 62px;
    background: var(--bar);
    display: flex; align-items: center;
    padding-left: 57px;
    color: var(--lime);
    font-size: 37px; font-weight: 700;
    white-space: nowrap;
  }
  .contact-bar .divider { margin: 0 26px 0 30px; font-weight: 400; }
  .contact-bar svg { width: 34px; height: 34px; margin-right: 12px; }
</style>
</head>
<body>
  <div class="decal">
    <svg class="headline" viewBox="0 0 740 240">
      <polygon points="0,66 567,27 572,117 0,156" fill="var(--lime)"/>
      <polygon points="0,156 725,117 731,179 0,230" fill="var(--lime)"/>
      <text x="29" y="131" font-size="66" textLength="508" lengthAdjust="spacingAndGlyphs" transform="rotate(-3.8 29 131)">Ihr Spezialist für</text>
      <text x="19" y="211" font-size="42" textLength="692" lengthAdjust="spacingAndGlyphs" transform="rotate(-3 19 211)">industrielle Automationslösungen</text>
    </svg>

    <div class="brand">
      <div class="brand-name">tk fertigwerk</div>
      <div class="brand-claim">Software für Ihre Anlagen</div>
    </div>

    <ul class="services">
      <li><svg viewBox="0 0 24 24"><circle cx="12" cy="12" r="12" fill="var(--ink)"/><path d="M6.5 12.5l3.8 3.6 7.2-7.6" fill="none" stroke="#fff" stroke-width="2.4" stroke-linecap="round" stroke-linejoin="round"/></svg>Roboter Programmierung und Inbetriebnahme</li>
      <li><svg viewBox="0 0 24 24"><circle cx="12" cy="12" r="12" fill="var(--ink)"/><path d="M6.5 12.5l3.8 3.6 7.2-7.6" fill="none" stroke="#fff" stroke-width="2.4" stroke-linecap="round" stroke-linejoin="round"/></svg>Roboter Schulungen für KRONA inhouse und extern</li>
      <li><svg viewBox="0 0 24 24"><circle cx="12" cy="12" r="12" fill="var(--ink)"/><path d="M6.5 12.5l3.8 3.6 7.2-7.6" fill="none" stroke="#fff" stroke-width="2.4" stroke-linecap="round" stroke-linejoin="round"/></svg>KRONA Roboter Inspektion, Wartung und Reparatur</li>
    </ul>

    <div class="contact-bar">
      <span class="web">www.tk-fertigwerk.net</span>
      <span class="divider">|</span>
      <svg viewBox="0 0 24 24"><path fill="var(--lime)" d="M6.6 10.8c1.4 2.8 3.8 5.2 6.6 6.6l2.2-2.2c.3-.3.7-.4 1-.2 1.1.4 2.3.6 3.6.6.6 0 1 .4 1 1V20c0 .6-.4 1-1 1C10.6 21 3 13.4 3 4c0-.6.4-1 1-1h3.5c.6 0 1 .4 1 1 0 1.3.2 2.5.6 3.6.1.3 0 .7-.2 1z"/></svg>
      <span class="phone">+49 (0)6123–45 67 89</span>
    </div>
  </div>
</body>
</html>
```